v eLiquid Label

We are an electronic cigarette eLiquid manufacturer with an outdated label design which needs to be updated and become more modern. All information listed on the label cannot be changed or removed.

There are 4 colour coding on the labels that cannot change.
0mg is white
12mg is yellow
18mg is blue
24mg is red

We prefer a blue type background however are not committed to it with the proper design however if a new colour is chosen it must compliment the colour band for each colour coding

The "dots" on the front of the bottle need to be larger.

The "V" on the front needs to be in this font however we can accept slight changes to it for effect.

Issues we are facing:
The 0mg and the 18mg look too close in colour and need to be completely different in colouring.

The background colouring is too dark and you cannot see the 50/50 in the watermark.

Reason: We have not received a design which is suitable to our needs. We have see a few close ones however not exact. Thanks

Reason: I was forced to go out of country for a family emergency and to be fair I am extending the deadline

```html
<!DOCTYPE html>
<html lang="en">
<head>
<meta charset="utf-8">
<title>Vela e-liquid Sweet Tobacco label range</title>
<link rel="stylesheet" href="https://fonts.googleapis.com/css2?family=Archivo:wght@300;400;700;800&display=swap">
<style>
  :root {
    --canvas: #ffffff;
    --body-light: #ffffff;
    --body-mid: #ececec;
    --body-dark: #cfcfcf;
    --ink: #3a3a3a;
    --ink-soft: #8a8a8a;
    --zero: #c4c4c4;
    --zero-band: #f4f4f4;
    --yellow: #e2b21c;
    --blue: #1f57a6;
    --red: #c8262a;
    --band-text-light: #ffffff;
  }
  * { box-sizing: border-box; margin: 0; padding: 0; }
  html, body { width: 1200px; height: 738px; overflow: hidden; }
  body {
    background: var(--canvas);
    font-family: "Archivo", Arial, sans-serif;
    color: var(--ink);
    position: relative;
  }
  .label-range {
    position: absolute;
    left: 0; top: 0;
    width: 1200px; height: 738px;
  }
  .label {
    position: absolute;
    top: 262px;
    width: 232px;
    height: 228px;
    display: flex;
    flex-direction: column;
    box-shadow: 0 1px 3px rgba(0,0,0,.12);
    --tone: var(--zero);
    --band: var(--zero);
    --band-ink: var(--band-text-light);
  }
  .label--zero   { left: 106px; --tone: var(--zero);  --band: var(--zero-band); --band-ink: var(--ink); }
  .label--12     { left: 356px; --tone: var(--yellow); --band: var(--yellow); --band-ink: var(--ink); }
  .label--18     { left: 606px; --tone: var(--blue);   --band: var(--blue); }
  .label--24     { left: 846px; --tone: var(--red);    --band: var(--red); }

  .band {
    height: 18px;
    background: var(--band);
    color: var(--band-ink);
    font-weight: 700;
    font-size: 10px;
    letter-spacing: .04em;
    display: flex;
    justify-content: space-around;
    align-items: center;
    white-space: nowrap;
    overflow: hidden;
  }
  .label--zero .band { border-top: 1px solid #e0e0e0; border-bottom: 1px solid #e0e0e0; }

  .label-body {
    flex: 1;
    display: flex;
    background: radial-gradient(ellipse at 45% 40%, var(--body-light) 0%, var(--body-mid) 55%, var(--body-dark) 100%);
  }
  .side-panel {
    width: 34px;
    padding: 8px 3px;
    font-size: 6px;
    line-height: 1.45;
    color: var(--ink);
    background: rgba(255,255,255,.75);
    overflow: hidden;
  }
  .side-panel strong { display: block; font-weight: 700; }
  .side-panel--left { text-align: right; }
  .side-panel--right { text-align: left; }

  .front {
    flex: 1;
    position: relative;
  }
  .strength {
    position: absolute;
    left: 6px; top: 70px;
    font-size: 22px;
    font-weight: 400;
    color: var(--tone);
  }
  .label--zero .strength { font-size: 15px; top: 76px; color: var(--ink); }
  .brand {
    position: absolute;
    left: 36px; top: 26px;
    display: flex;
    align-items: center;
    gap: 5px;
  }
  .brand-dot {
    width: 12px; height: 12px;
    border-radius: 50%;
    background: var(--tone);
  }
  .brand-name {
    font-size: 36px;
    font-weight: 800;
    color: var(--tone);
    letter-spacing: .01em;
  }
  .product-type {
    position: absolute;
    left: 58px; top: 82px;
    font-size: 20px;
    font-weight: 300;
    color: var(--ink-soft);
  }
  .volume {
    position: absolute;
    right: 8px; top: 106px;
    font-size: 7px;
    color: var(--ink-soft);
  }
  .flavour {
    position: absolute;
    left: 6px; bottom: 14px;
    font-size: 17px;
    letter-spacing: -.01em;
    color: var(--ink);
    white-space: nowrap;
  }
  .flavour .light { font-weight: 300; }
  .flavour .bold { font-weight: 700; }
</style>
</head>
<body>
<main class="label-range">

  <section class="label label--zero">
    <div class="band"><span>FREE</span><span>NICOTINE</span><span>FREE</span></div>
    <div class="label-body">
      <div class="side-panel side-panel--left"><strong>NOTICE</strong>Keep out of reach of children and pets. Do not swallow. Store cool and dry.</div>
      <div class="front">
        <span class="strength">zero</span>
        <div class="brand"><span class="brand-dot"></span><span class="brand-name">VELA</span></div>
        <span class="product-type">e-liquid</span>
        <span class="volume">30 ml</span>
        <p class="flavour"><span class="light">SWEET</span> <span class="bold">TOBACCO</span></p>
      </div>
      <div class="side-panel side-panel--right">Use in e-cigarettes only. Call poison control if swallowed.</div>
    </div>
    <div class="band"><span>NICOTINE</span><span>ZÉRO</span><span>NICOTINE</span></div>
  </section>

  <section class="label label--12">
    <div class="band"><span>12 mg/ml</span><span>12 mg/ml</span><span>12 mg/ml</span></div>
    <div class="label-body">
      <div class="side-panel side-panel--left"><strong>NOTICE</strong>Keep out of reach of children and pets. Do not swallow. Store cool and dry.</div>
      <div class="front">
        <span class="strength">12</span>
        <div class="brand"><span class="brand-dot"></span><span class="brand-name">VELA</span></div>
        <span class="product-type">e-liquid</span>
        <span class="volume">30 ml</span>
        <p class="flavour"><span class="light">SWEET</span> <span class="bold">TOBACCO</span></p>
      </div>
      <div class="side-panel side-panel--right">Use in e-cigarettes only. Call poison control if swallowed.</div>
    </div>
    <div class="band"><span>POISON</span><span>DANGER</span><span>POISON</span></div>
  </section>

  <section class="label label--18">
    <div class="band"><span>18 mg/ml</span><span>18 mg/ml</span><span>18 mg/ml</span></div>
    <div class="label-body">
      <div class="side-panel side-panel--left"><strong>NOTICE</strong>Keep out of reach of children and pets. Do not swallow. Store cool and dry.</div>
      <div class="front">
        <span class="strength">18</span>
        <div class="brand"><span class="brand-dot"></span><span class="brand-name">VELA</span></div>
        <span class="product-type">e-liquid</span>
        <span class="volume">30 ml</span>
        <p class="flavour"><span class="light">SWEET</span> <span class="bold">TOBACCO</span></p>
      </div>
      <div class="side-panel side-panel--right">Use in e-cigarettes only. Call poison control if swallowed.</div>
    </div>
    <div class="band"><span>POISON</span><span>DANGER</span><span>POISON</span></div>
  </section>

  <section class="label label--24">
    <div class="band"><span>24 mg/ml</span><span>24 mg/ml</span><span>24 mg/ml</span></div>
    <div class="label-body">
      <div class="side-panel side-panel--left"><strong>NOTICE</strong>Keep out of reach of children and pets. Do not swallow. Store cool and dry.</div>
      <div class="front">
        <span class="strength">24</span>
        <div class="brand"><span class="brand-dot"></span><span class="brand-name">VELA</span></div>
        <span class="product-type">e-liquid</span>
        <span class="volume">30 ml</span>
        <p class="flavour"><span class="light">SWEET</span> <span class="bold">TOBACCO</span></p>
      </div>
      <div class="side-panel side-panel--right">Use in e-cigarettes only. Call poison control if swallowed.</div>
    </div>
    <div class="band"><span>POISON</span><span>DANGER</span><span>POISON</span></div>
  </section>

</main>
</body>
</html>
```